Design a modern, classy & professional business card for an online real estate agency, specializing in medium-luxury properties in Thailand and later in Singapore and UK.

Possible design ideas so far: (not essential)

- curved corner(s) to the card, white on front & turquoise on back or visa versa.

- front of card - clear and simple, company name in metallic grey/monochrome, logo graphic & company name on front in spot UV or embossed/debossed effect.

- back of card - large, close-cropped, 'ghost' patterns of the C-shaped curves of logo, or company name repeated on back of card in spot UV.

Target Market(s)

- young to middle-aged professionals mainly (but ideally should design should suit all)

- UK, US,EU,AUS & ASIAN mainly (but ideally should design should suit all countries)

Industry/Entity Type

Real Estate

Requirements
Must have
• THEME:
- Luxurious & Modern
- Clean & striking
- Unique & creative

INFO:
- Logo & company name on front
- Contact details on back:

Tobias Lindqvist
Managing Director

www.velmoraestates.example
www.velmoraestates-uk.example

Tel: 083-274-6190
email: tobias@velmoraestates.example

(contact details can be displayed in any order as suites design.)

Nice to have
• - curved corner(s) to the card, white on front & turquoise on back or visa versa.

Should not have
• - No generic images of properties, palm trees/coconut trees etc.

- No other other bold colors, except for main turquoise, grey, metallic white & black theme.

- No obvious business card templates

```html
<!DOCTYPE html>
<html lang="en">
<head>
<meta charset="utf-8">
<title>Velmora Estates – Business Card Front</title>
<link rel="stylesheet" href="https://fonts.googleapis.com/css2?family=Cormorant+Garamond:wght@500&family=Montserrat:wght@500;700&display=swap">
<style>
  :root {
    --page: #ffffff;
    --stage: #ececec;
    --card: #fbfbfb;
    --card-edge: #dedede;
    --metallic-grey: #b9b9b9;
    --mark-grey: #c6c6c6;
    --caption-grey: #8a8a8a;
  }
  * { margin: 0; padding: 0; box-sizing: border-box; }
  html, body {
    width: 1200px;
    height: 1000px;
    overflow: hidden;
    background: var(--page);
  }
  .sheet {
    position: relative;
    width: 1200px;
    height: 1000px;
  }
  .stage {
    position: absolute;
    left: 0;
    top: 163px;
    width: 1200px;
    height: 672px;
    background: var(--stage);
    display: flex;
    align-items: center;
    justify-content: center;
  }
  .card-front {
    width: 640px;
    height: 419px;
    background: var(--card);
    border: 1px solid var(--card-edge);
    border-radius: 34px;
    display: flex;
    align-items: center;
    justify-content: center;
  }
  .brand {
    display: flex;
    align-items: center;
    gap: 18px;
  }
  .brand-square {
    width: 104px;
    height: 104px;
    background: var(--mark-grey);
  }
  .brand-name {
    font-family: "Cormorant Garamond", Georgia, serif;
    font-weight: 500;
    color: var(--metallic-grey);
    line-height: 1;
  }
  .brand-name .word-main {
    display: block;
    font-size: 76px;
    letter-spacing: -1px;
  }
  .brand-name .word-sub {
    display: block;
    font-size: 21px;
    letter-spacing: 9px;
    margin-top: 4px;
    padding-left: 4px;
  }
  .spec-caption {
    position: absolute;
    left: 0;
    top: 898px;
    width: 1200px;
    text-align: center;
    font-family: "Montserrat", Arial, sans-serif;
    font-weight: 500;
    font-size: 16px;
    letter-spacing: 2.4px;
    color: var(--caption-grey);
    text-transform: uppercase;
  }
  .spec-caption strong { font-weight: 700; }
</style>
</head>
<body>
  <main class="sheet">
    <section class="stage">
      <div class="card-front">
        <div class="brand">
          <span class="brand-square"></span>
          <p class="brand-name">
            <span class="word-main">Velmora</span>
            <span class="word-sub">ESTATES</span>
          </p>
        </div>
      </div>
    </section>
    <p class="spec-caption"><strong>Front</strong> 84mm x 55mm&nbsp; Metallic grey debossed print logo</p>
  </main>
</body>
</html>
```